Corporate Web Redesign Project - coded

We would like redesign/refresh of our current site that would allow us to increase the depth of content and create a high quality impression for visitors.

Current site - http://corvanisystems.com/

A previous web redesign project has improved our site but it has not really reached the level we require.

Our customers are global, blue chip, organisations and a professional, corporate style of site is required.

Please note we would prefer a coded website to a just a design. We are happy to provide a zip of our current site if required.
Updates

                                   

Target Market(s)

Global oil and gas producers, KR, Tamberline, Orvadex etc.

Industry/Entity Type

It Professional

Requirements
Must have
• Design should support the level of content we currently have in the existing sitemap - although it should be expandable a site design for a large / complex site would not be appropriate

All current content / pages to be reflected in design

Must be visually appealing

Intuitive and clear navigation that is expandable

Display a high level of professionalism

Use a consistent palette of colours that complements our logo

Clean and organized layout

A way to capture visitor’s information or Call to action (i.e. contact link or form) on every page

Prominent Contact Information
Should not have
• Flash

```html
<!DOCTYPE html>
<html lang="en">
<head>
<meta charset="utf-8">
<title>Corvani Systems – Home Sections</title>
<link rel="stylesheet" href="https://fonts.googleapis.com/css2?family=Open+Sans:ital,wght@0,400;0,600;0,700;1,400&display=swap">
<style>
:root{
  --ink:#2b2b2b;
  --body:#666;
  --muted:#c4c4c4;
  --teal:#33b1be;
  --teal-dark:#2a9ba7;
  --line:#dcdcdc;
  --panel:#fcfcfc;
  --tab-off:#f6f6f6;
  --stripe:#e6e6e6;
}
*{box-sizing:border-box;margin:0;padding:0}
html,body{width:1200px;height:1000px;overflow:hidden;background:#fff}
body{font-family:"Open Sans",Arial,sans-serif;color:var(--body);position:relative}
.section-title{position:absolute;display:flex;align-items:center;gap:18px;height:24px}
.section-title h2{font-size:18px;font-weight:400;color:var(--ink);white-space:nowrap;letter-spacing:.1px}
.section-title .rule{flex:1;height:12px;background:repeating-linear-gradient(135deg,var(--stripe) 0 2px,transparent 2px 5px)}
.projects-title{left:96px;top:17px;width:1010px}
.project{position:absolute;top:61px;width:320px;text-align:center}
.project .photo{width:320px;height:213px}
.project h3{font-size:14px;font-weight:400;color:var(--ink);margin-top:16px}
.project p{font-size:12px;font-style:italic;color:var(--muted);margin-top:4px}
.rig-yard{background:linear-gradient(180deg,#6f6f8e 0%,#b592a8 45%,#3a3540 70%,#1c1c20 100%)}
.pump-jack{background:linear-gradient(180deg,#e0401c 0%,#f67a1e 50%,#c8361a 80%,#2a0e08 100%)}
.offshore{background:linear-gradient(180deg,#e4707a 0%,#c4607e 40%,#5a4672 65%,#2f2c58 100%)}
.tabs{position:absolute;left:96px;top:380px;width:492px}
.tab-row{display:flex;height:37px}
.tab{flex:1;display:flex;align-items:center;justify-content:center;gap:7px;font-size:13px;color:var(--ink);border:1px solid var(--line)}
.tab.active{background:#fff;border-top:2px solid var(--teal);border-bottom:none}
.tab.idle{background:var(--tab-off);border-left:none}
.tab-body{padding-top:19px}
.tab-body p{font-size:13px;line-height:20px;margin-bottom:15px}
.services-title{left:613px;top:381px;width:493px}
.services{position:absolute;left:613px;top:423px;list-style:none}
.services li{display:flex;align-items:center;gap:8px;height:30px;font-size:13px}
.services svg{flex:none}
.callout{position:absolute;left:96px;top:614px;width:1010px;height:108px;background:var(--panel);border:1px solid var(--line);border-left:2px solid var(--teal);padding:27px 28px}
.callout h2{font-size:22px;font-weight:400;color:var(--ink)}
.callout p{font-size:12.5px;margin-top:9px}
.callout .cta{position:absolute;right:28px;top:28px;width:132px;height:40px;background:var(--teal);border:1px solid var(--teal-dark);border-radius:2px;color:#fff;font-size:13.5px;font-weight:600;display:flex;align-items:center;justify-content:center;text-decoration:none}
.clients-title{left:96px;top:763px;width:1010px}
.clients{position:absolute;left:83px;top:815px;width:1030px;display:grid;grid-template-columns:repeat(5,206px);grid-auto-rows:100px}
.client{display:flex;align-items:center;justify-content:center;gap:6px;font-size:17px;font-weight:600;height:60px}
.client .dot{width:12px;height:12px;border-radius:50%}
.c1{color:#a9c7e6}.c1 .dot{background:#a9c7e6}
.c2{color:#e1b7a0}
.c3{color:#f0e1a3}
.c4{color:#c9b8bd}.c4 .dot{background:#e8b9c2}
.c5{color:#bfe39a}.c5 .dot{background:#cdeaa5}
.c6{color:#a7c4e0}
.c7{color:#b9cdbf}
</style>
</head>
<body>

<div class="section-title projects-title"><h2>Recent Projects</h2><span class="rule"></span></div>

<div class="project" style="left:96px">
  <div class="photo rig-yard" role="img" aria-label="Drilling rigs and cranes in a yard at dusk"></div>
  <h3>Lorem Ipsum</h3><p>Dolor sit amet</p>
</div>
<div class="project" style="left:440px">
  <div class="photo pump-jack" role="img" aria-label="Oil pump jack silhouetted against an orange sunset"></div>
  <h3>Lorem Ipsum</h3><p>Dolor sit amet</p>
</div>
<div class="project" style="left:784px">
  <div class="photo offshore" role="img" aria-label="Offshore oil platform at sea under a pink sunset"></div>
  <h3>Lorem Ipsum</h3><p>Dolor sit amet</p>
</div>

<div class="tabs">
  <div class="tab-row">
    <div class="tab active">
      <svg width="12" height="12" viewBox="0 0 12 12"><rect x="0" y="5" width="3" height="7" fill="#333"/><path d="M4 5 L7 1 Q8.5 1 8 3.5 L7.5 5 H11 Q12 5 11.6 6.5 L10.5 11 Q10.2 12 9 12 H4 Z" fill="#333"/></svg>
      About Us
    </div>
    <div class="tab idle">
      <svg width="14" height="10" viewBox="0 0 14 10"><rect x="0.5" y="0.5" width="13" height="9" fill="none" stroke="#444"/><circle cx="7" cy="5" r="2.2" fill="#444"/></svg>
      Latest News
    </div>
  </div>
  <div class="tab-body">
    <p>From early phase evaluation through planning, execution and post analysis of wells, we deliver the tools, processes and people required to facilitate major performance improvement and cost savings.</p>
    <p>Our solutions are used in more than 30 countries to support operations ranging from a single well to global deployments with Major Operators.</p>
  </div>
</div>

<div class="section-title services-title"><h2>Services &amp; Consulting</h2><span class="rule"></span></div>
<ul class="services">
  <li><svg width="20" height="20" viewBox="0 0 20 20"><circle cx="10" cy="10" r="10" fill="var(--teal)"/><path d="M5.5 10.2 L8.6 13 L14.5 7" fill="none" stroke="#fff" stroke-width="2.2"/></svg>Process Mapping and Gap Analysis</li>
  <li><svg width="20" height="20" viewBox="0 0 20 20"><circle cx="10" cy="10" r="10" fill="var(--teal)"/><path d="M5.5 10.2 L8.6 13 L14.5 7" fill="none" stroke="#fff" stroke-width="2.2"/></svg>Change Management</li>
  <li><svg width="20" height="20" viewBox="0 0 20 20"><circle cx="10" cy="10" r="10" fill="var(--teal)"/><path d="M5.5 10.2 L8.6 13 L14.5 7" fill="none" stroke="#fff" stroke-width="2.2"/></svg>Project Management</li>
  <li><svg width="20" height="20" viewBox="0 0 20 20"><circle cx="10" cy="10" r="10" fill="var(--teal)"/><path d="M5.5 10.2 L8.6 13 L14.5 7" fill="none" stroke="#fff" stroke-width="2.2"/></svg>Training</li>
  <li><svg width="20" height="20" viewBox="0 0 20 20"><circle cx="10" cy="10" r="10" fill="var(--teal)"/><path d="M5.5 10.2 L8.6 13 L14.5 7" fill="none" stroke="#fff" stroke-width="2.2"/></svg>Business and Technical Consulting and Support</li>
</ul>

<div class="callout">
  <h2>The Business Of Drilling Wells</h2>
  <p>The success of the initiative is only as good as the process and the training of the people working the system.</p>
  <a class="cta" href="#">Know More!</a>
</div>

<div class="section-title clients-title"><h2>Our Clients</h2><span class="rule"></span></div>
<div class="clients">
  <div class="client c1"><span class="dot"></span>Orvadex</div>
  <div class="client c2">Marrowfield</div>
  <div class="client c3">Sollent</div>
  <div class="client c4"><span class="dot"></span>Brackwater</div>
  <div class="client c5"><span class="dot"></span>KR</div>
  <div class="client c6">Veyrana</div>
  <div class="client c7">Halden</div>
</div>

</body>
</html>
```